Brochure and business Design Project

I need to designee brochures for my company and need material helps me to market my business.
I own a corporate housing company and accommodations services which is we rent out furnished apartment for short term lease 30 days or more and we provider many services for international patient who come to Houston Brightwater medical center for medical treatment , pleasure , business or visit we also provide help with limousine service airport pick ups , cleaning services , concierge service , car rental services , prepaid services , immigration stay extend service .
explain about services we provide and talk about our goal and the company, i need inviting colors we accommodating people like hotline and etc, my logo must be change to fit with new design, i do not want to copy and past what i have on my website or on what i sent i need better story and something to help me marking my hosting business

Target Market(s)

business material

Industry/Entity Type

Accommodation

Colors

Designer to choose colors to be used in the design.

Requirements
Must have
• explain about services we provide and talk about our goal and the company, i need inviting colors we accommodating people like hotline and etc, my logo must be change to fit with new design, i do not want to copy and past what i have on my website or on what i sent i need better story and something to help me marking my business . we accommodate patient from all over the planet who comes for medicl treatment at Brightwater medical center
Nice to have
• different langue's
Should not have
• any sexual , or religion signs

```html
<!DOCTYPE html>
<html lang="en">
<head>
<meta charset="utf-8">
<title>Harborline Residences – Tri-fold Brochure</title>
<link href="https://fonts.googleapis.com/css2?family=Montserrat:wght@500;600;700&family=Raleway:wght@400;500;600;700&display=swap" rel="stylesheet">
<style>
:root{
  --magenta:#b3245f;
  --magenta-dark:#8a1a48;
  --teal:#2c3e41;
  --teal-dark:#223235;
  --paper:#ffffff;
  --paper-soft:#eef0f1;
  --ink:#3d3d42;
  --ink-soft:#6b6b72;
  --stage:#3a3b3e;
}
*{box-sizing:border-box;margin:0;padding:0}
html,body{width:1200px;height:2267px;overflow:hidden;background:var(--stage)}
body{font-family:"Raleway",Arial,sans-serif;color:var(--ink)}
.canvas{position:relative;width:1200px;height:2267px}
.spread{position:absolute;left:60px;width:1080px;height:1040px;display:flex;box-shadow:0 18px 40px rgba(0,0,0,.45)}
.spread--outside{top:60px}
.spread--inside{top:1167px}
.panel{position:relative;width:360px;height:1040px;overflow:hidden;background:var(--paper)}
.panel + .panel{border-left:1px solid rgba(0,0,0,.08)}
.photo{position:absolute;left:0;width:100%}
.shape{position:absolute;left:0;top:0;width:360px;height:1040px}

/* outside – back flap */
.photo--lounge{top:0;height:660px;background:linear-gradient(160deg,#c9ccc9 0%,#9da3a2 45%,#6d706c 100%)}
.back-intro{position:absolute;left:34px;right:34px;top:770px;color:#fff;font-size:17px;line-height:1.45;text-align:center;font-weight:500}

/* outside – contact */
.photo--skyline{top:0;height:820px;background:linear-gradient(180deg,#f1c890 0%,#d7b79a 22%,#8ea6b6 50%,#6f7f86 78%,#4f5e5f 100%)}
.map-spot{position:absolute;left:205px;top:700px;width:124px;height:124px;border-radius:50%;background:linear-gradient(140deg,#f2f2ee,#d9dcd8);border:3px solid #fff}
.contact{position:absolute;left:0;right:0;top:880px;text-align:center;color:#fff;font-size:15px;line-height:1.55}
.contact__label{font-weight:600;font-size:16px}

/* outside – cover */
.photo--cover{top:0;height:640px;background:linear-gradient(180deg,#f3d3a2 0%,#cdb7a3 20%,#90a8ba 45%,#6f8089 75%,#5c6a6b 100%)}
.cover-title{position:absolute;left:40px;top:660px;width:320px;color:#fff;font-family:"Montserrat",Arial,sans-serif;font-weight:600;font-size:27px;line-height:1.15;text-align:center;transform:rotate(-24deg);transform-origin:center}
.cover-title small{display:block;font-size:23px;font-weight:500}
.brand{position:absolute;left:0;right:0;top:905px;text-align:center}
.brand__name{font-family:"Raleway",Arial,sans-serif;font-weight:700;font-size:27px;color:var(--magenta);letter-spacing:-.3px}
.brand__tag{margin-top:4px;font-size:13px;color:var(--ink-soft);letter-spacing:1px}

/* inside – about */
.panel--about{background:var(--magenta)}
.about{position:absolute;left:30px;right:28px;top:54px;color:#fff;font-size:16.5px;line-height:1.45;font-weight:500}
.about p + p{margin-top:20px}
.photo--garden{top:820px;height:220px;background:linear-gradient(180deg,#a9c3d0 0%,#7f9a7a 45%,#4e6a3f 100%)}

/* inside – services */
.panel--services{background:linear-gradient(180deg,#f7f7f8,#e6e8ea)}
.services{position:absolute;left:34px;right:28px;top:54px}
.services__title{font-family:"Montserrat",Arial,sans-serif;font-weight:700;font-size:22px;line-height:1.2;color:var(--ink)}
.services__lead{font-size:14.5px;line-height:1.45;margin-top:6px}
.services__lead strong{font-family:"Montserrat",Arial,sans-serif;font-size:18px}
.services__text{margin-top:22px;font-size:14.5px;line-height:1.5;text-align:center}
.services__sub{margin-top:34px;font-family:"Montserrat",Arial,sans-serif;font-weight:700;font-size:18px;text-decoration:underline;text-underline-offset:4px}
.services__list{margin-top:14px;list-style:none;font-size:15.5px;line-height:1.75}
.services__list li::before{content:"• ";color:var(--ink)}
.photo--studio{top:860px;height:180px;background:linear-gradient(180deg,#3f4546 0%,#1f2324 100%)}

/* inside – amenities */
.panel--amenities{background:linear-gradient(180deg,#f4f4f5,#e4e6e7)}
.amenities{position:absolute;left:24px;right:20px;top:52px;list-style:none}
.amenity{display:flex;align-items:flex-start;gap:14px;height:96px}
.amenity svg{flex:0 0 42px;width:42px;height:42px;stroke:var(--magenta);fill:none;stroke-width:2.4;stroke-linecap:round;stroke-linejoin:round}
.amenity__body{text-align:center;flex:1}
.amenity__name{font-weight:700;font-size:15px;color:var(--ink)}
.amenity__note{font-size:12.5px;line-height:1.35;color:var(--ink-soft)}
.photo--gym{top:700px;height:340px;background:linear-gradient(180deg,#c9c1b4 0%,#9a8c77 45%,#5d7170 100%)}
</style>
</head>
<body>
<div class="canvas">

  <!-- Outside: back flap, contact panel, cover -->
  <section class="spread spread--outside">
    <article class="panel panel--back">
      <div class="photo photo--lounge" role="img" aria-label="Photo of a bright apartment lounge with a white sofa by tall windows"></div>
      <svg class="shape" viewBox="0 0 360 1040" aria-hidden="true">
        <polygon points="0,640 360,590 360,1040 0,1040" fill="var(--magenta)"/>
        <polygon points="250,605 360,590 360,700" fill="var(--magenta-dark)"/>
      </svg>
      <p class="back-intro">Featuring free WiFi and air conditioning, Harborline Residences Corporate Housing is situated in Houston. Lakeview Stadium is 1 km away. Free private parking is available on site.</p>
    </article>

    <article class="panel panel--contact">
      <div class="photo photo--skyline" role="img" aria-label="Photo of a city skyline with office towers at sunset"></div>
      <svg class="shape" viewBox="0 0 360 1040" aria-hidden="true">
        <polygon points="0,850 360,760 360,1040 0,1040" fill="var(--teal)"/>
        <polygon points="0,850 90,828 0,900" fill="var(--teal-dark)"/>
      </svg>
      <div class="map-spot" role="img" aria-label="Small street map showing the location"></div>
      <svg style="position:absolute;left:256px;top:742px" width="22" height="30" viewBox="0 0 22 30" aria-hidden="true">
        <path d="M11 1C5.5 1 1.5 5 1.5 10.5 1.5 18 11 29 11 29s9.5-11 9.5-18.5C20.5 5 16.5 1 11 1z" fill="var(--magenta)"/>
        <circle cx="11" cy="10.5" r="3.6" fill="#fff"/>
      </svg>
      <div class="contact">
        <p class="contact__label">Contact</p>
        <p>+1 555 014 2290</p>
        <p>stay@harborlineresidences.com</p>
        <p>Maple Crest Drive Houston, TX 77000</p>
        <p>United States of America</p>
      </div>
    </article>

    <article class="panel panel--cover">
      <div class="photo photo--cover" role="img" aria-label="Photo of downtown office towers under a warm evening sky"></div>
      <svg class="shape" viewBox="0 0 360 1040" aria-hidden="true">
        <polygon points="0,800 360,560 360,1040 0,1040" fill="var(--paper)"/>
        <polygon points="0,800 360,560 360,700 0,900" fill="var(--paper)"/>
        <polygon points="0,690 360,450 360,660 0,880" fill="var(--magenta)"/>
        <polygon points="0,690 120,610 0,760" fill="var(--magenta-dark)"/>
      </svg>
      <h1 class="cover-title">HARBORLINE RESIDENCES<small>Corporate Housing</small></h1>
      <div class="brand">
        <p class="brand__name">harborline residences</p>
        <p class="brand__tag">Corporate Housing</p>
      </div>
    </article>
  </section>

  <!-- Inside: about, services, amenities -->
  <section class="spread spread--inside">
    <article class="panel panel--about">
      <div class="about">
        <p>All units have a seating area. Some units include a dining area and/or balcony. All units feature a kitchen fitted with a dishwasher and oven. A microwave is also provided, as well as a coffee machine and a kettle. There is a private bathroom with a bath and bidet in every unit. Bed linen is featured.</p>
        <p>Harborline Residences Corporate Housing also includes a fitness centre.</p>
        <p>You can play billiards at the property, and car hire is available. Lakeview Park is 1.3 km from Harborline Residences Corporate Housing, while Riverside Stadium is 2.7 km from the property. The nearest airport is Southgate Field Airport, 14 km from Harborline Residences Corporate Housing.</p>
      </div>
      <div class="photo photo--garden" role="img" aria-label="Photo of a garden pond with palm trees and a fountain"></div>
      <svg class="shape" viewBox="0 0 360 1040" aria-hidden="true">
        <path d="M0,800 Q180,860 360,830 L360,840 Q180,872 0,815 Z" fill="var(--magenta)"/>
      </svg>
    </article>

    <article class="panel panel--services">
      <div class="services">
        <h2 class="services__title">Harborline Residences</h2>
        <p class="services__lead"><strong>services</strong> which is we rent out furnished apartment for short term lease 30 days</p>
        <p class="services__text">We provider many services for international patient who come to Houston Brightwater medical center for medical treatment, pleasure, business or visit.</p>
        <h3 class="services__sub">We also provide help with</h3>
        <ul class="services__list">
          <li>Limousine service</li>
          <li>Airport pickups</li>
          <li>Cleaning services</li>
          <li>Concierge service</li>
          <li>Car rental services</li>
          <li>Prepaid services</li>
          <li>Immigrations stay extend service</li>
        </ul>
      </div>
      <div class="photo photo--studio" role="img" aria-label="Photo of a dark fitness studio with a training bag"></div>
      <svg class="shape" viewBox="0 0 360 1040" aria-hidden="true">
        <path d="M0,850 Q180,900 360,860 L360,858 L0,858 Z" fill="#e7e9eb"/>
      </svg>
    </article>

    <article class="panel panel--amenities">
      <ul class="amenities">
        <li class="amenity">
          <svg viewBox="0 0 42 42"><path d="M6 16a22 22 0 0 1 30 0"/><path d="M11 22a14 14 0 0 1 20 0"/><path d="M16 28a7 7 0 0 1 10 0"/><circle cx="21" cy="33" r="1.6" fill="var(--magenta)"/></svg>
          <div class="amenity__body"><p class="amenity__name">Internet</p><p class="amenity__note">WiFi is available in the hotel rooms and is free of charge.</p></div>
        </li>
        <li class="amenity">
          <svg viewBox="0 0 42 42"><rect x="5" y="17" width="32" height="12" rx="3"/><path d="M10 17l4-8h14l4 8"/><circle cx="12" cy="31" r="3"/><circle cx="30" cy="31" r="3"/></svg>
          <div class="amenity__body"><p class="amenity__name">Parking</p><p class="amenity__note">Free private parking is available on site (reservation is not needed).</p></div>
        </li>
        <li class="amenity">
          <svg viewBox="0 0 42 42"><ellipse cx="21" cy="28" rx="8" ry="7" fill="var(--magenta)"/><circle cx="11" cy="18" r="3.5" fill="var(--magenta)"/><circle cx="31" cy="18" r="3.5" fill="var(--magenta)"/><circle cx="16" cy="10" r="3.5" fill="var(--magenta)"/><circle cx="26" cy="10" r="3.5" fill="var(--magenta)"/></svg>
          <div class="amenity__body"><p class="amenity__name">Pets</p><p class="amenity__note">Pets are allowed on request. Charges may apply.</p></div>
        </li>
        <li class="amenity">
          <svg viewBox="0 0 42 42"><path d="M14 6v20M26 6v20M14 12h12M14 19h12"/><path d="M4 30q4-3 8 0t8 0 8 0 8 0"/><path d="M4 36q4-3 8 0t8 0 8 0 8 0"/></svg>
          <div class="amenity__body"><p class="amenity__name">Pool</p><p class="amenity__note">Outdoor Pool – FREE. Outdoor Pool (seasonal) – FREE.</p></div>
        </li>
        <li class="amenity">
          <svg viewBox="0 0 42 42"><path d="M12 5v10a4 4 0 0 0 8 0V5M16 5v32"/><path d="M30 37V5c-4 3-5 9-4 16h4"/></svg>
          <div class="amenity__body"><p class="amenity__name">Food &amp; Drink</p><p class="amenity__note">BBQ Facilities</p></div>
        </li>
        <li class="amenity">
          <svg viewBox="0 0 42 42"><circle cx="13" cy="10" r="4"/><circle cx="29" cy="10" r="4"/><circle cx="21" cy="22" r="3"/><path d="M7 36V22a6 6 0 0 1 12 0"/><path d="M23 22a6 6 0 0 1 12 0v14"/><path d="M17 36v-6a4 4 0 0 1 8 0v6"/></svg>
          <div class="amenity__body"><p class="amenity__name">Family Friendly</p><p class="amenity__note">Family Rooms</p></div>
        </li>
      </ul>
      <div class="photo photo--gym" role="img" aria-label="Photo of a fitness room with exercise bikes and a bedroom below"></div>
      <svg class="shape" viewBox="0 0 360 1040" aria-hidden="true">
        <path d="M0,700 L0,740 Q180,690 360,700 Z" fill="#e9ebec"/>
      </svg>
    </article>
  </section>

</div>
</body>
</html>
```